Postcard needed for expert witness service

Looking for a professional postcard that will be mailed to personal injury lawyers / law firms to introduce my expert witness services.

Target Market(s)

Law firms, personal injury lawyers

Industry/Entity Type

Expert witness, law

Font styles to use
Sans Serif

Requirements
Must have
• Logo: The Frost Counsel [Main Heading]Do you handle snow and ice related slip and falls? Darrel is one of the top snow industry experts in the country! [Following should be in a list type fashion, possibly bulleted]Darrel's credentials: Accredited Winter Practitioner (AWP), past WRTA board member and chair, former ISO 9001 certified snow company owner , 32 years in the industry. (555) 284-3917 NOTES: Postcard will be 4" x 6" Please use both sides however must have room for labels and stamp
Should not have
• Wouldn't suggest using both photos on same side. Honestly, feel free to only use one of the slip and fall photos if it works out better. Thanks!

```html
<!DOCTYPE html>
<html lang="en">
<head>
<meta charset="utf-8">
<title>The Frost Counsel – Postcard</title>
<link href="https://fonts.googleapis.com/css2?family=Fira+Sans:wght@300;400;700;800&display=swap" rel="stylesheet">
<style>
  :root {
    --backdrop: #b3b3b3;
    --ink: #111111;
    --white: #ffffff;
    --footer: #000000;
    --panel: #4a4a4a;
    --tick: #9a9a9a;
    --stamp-line: #cfcfcf;
    --address: #2a2a2a;
  }
  * { box-sizing: border-box; margin: 0; padding: 0; }
  html, body { width: 1200px; height: 904px; overflow: hidden; }
  body {
    position: relative;
    background: var(--backdrop);
    font-family: "Fira Sans", Arial, sans-serif;
  }
  .postcard {
    position: absolute;
    width: 493px;
    height: 329px;
    overflow: hidden;
  }
  .postcard--front { left: 215px; top: 98px; }
  .postcard--back  { left: 492px; top: 478px; }

  .photo-area { position: absolute; left: 0; top: 0; width: 493px; height: 299px; }
  .postcard--front .photo-area {
    background:
      radial-gradient(ellipse 160px 130px at 300px 210px, #5a4a45 0%, rgba(90,74,69,0) 100%),
      linear-gradient(100deg, #7f766d 0%, #9b938a 30%, #b8b2ab 52%, #e9ecee 70%, #f7f8f9 100%);
  }
  .postcard--back .photo-area {
    background:
      radial-gradient(ellipse 120px 150px at 160px 150px, #3e5478 0%, rgba(62,84,120,0) 100%),
      radial-gradient(ellipse 110px 60px at 320px 240px, #8d8f93 0%, rgba(141,143,147,0) 100%),
      linear-gradient(95deg, #6b5a4f 0%, #7d8da6 22%, #c9cbce 50%, #eeeeee 75%, #f4f4f4 100%);
  }

  .headline {
    position: absolute; left: 20px; top: 21px; width: 270px;
    color: var(--white); font-weight: 700; font-size: 21.5px; line-height: 27px;
  }
  .intro {
    position: absolute; left: 20px; top: 83px; width: 260px;
    color: var(--white); font-weight: 400; font-size: 14px; line-height: 18px;
  }

  .brand {
    position: absolute; color: var(--ink); font-weight: 300;
    text-transform: uppercase; text-align: center; line-height: 1;
  }
  .postcard--front .brand { left: 300px; top: 24px; width: 178px; font-size: 25px; letter-spacing: 0.5px; }
  .postcard--back .brand { left: 272px; top: 24px; width: 134px; font-size: 18.5px; letter-spacing: 0.3px; }

  .credentials-panel { position: absolute; left: 0; top: 0; }
  .credentials {
    position: absolute; left: 20px; top: 172px; width: 160px; color: var(--white);
  }
  .credentials h2 { font-size: 11px; font-weight: 700; margin-bottom: 3px; letter-spacing: 0.1px; }
  .credentials ul { list-style: none; }
  .credentials li {
    position: relative; padding-left: 13px; font-size: 10.5px; font-weight: 400;
    line-height: 13px; margin-bottom: 4px;
  }
  .credentials li svg { position: absolute; left: 0; top: 2px; }

  .contact-bar {
    position: absolute; left: 0; bottom: 0; width: 493px; height: 30px;
    background: var(--footer); color: var(--white);
    display: flex; align-items: center; padding: 0 19px 0 20px;
    justify-content: space-between; font-size: 10.2px; font-weight: 400;
  }
  .contact-item { display: flex; align-items: center; gap: 3px; white-space: nowrap; }
  .contact-item strong { font-weight: 700; margin-right: 1px; }
  .contact-item .phone-number { font-weight: 700; }

  .return-address {
    position: absolute; left: 254px; top: 60px; width: 160px; text-align: right;
    font-size: 8.4px; color: var(--address); font-weight: 400;
  }
  .stamp-box {
    position: absolute; left: 418px; top: 19px; width: 53px; height: 50px;
    border: 1px solid var(--stamp-line); background: var(--white);
  }
</style>
</head>
<body>

  <section class="postcard postcard--front">
    <div class="photo-area" role="img" aria-label="Photo of a woman in a winter coat and knit hat slipping and falling on an icy, snowy sidewalk"></div>

    <svg class="credentials-panel" width="493" height="299" viewBox="0 0 493 299" aria-hidden="true">
      <defs>
        <linearGradient id="panelFade" x1="0" y1="0" x2="1" y2="0">
          <stop offset="0" stop-color="#474747" stop-opacity="0.97"/>
          <stop offset="0.7" stop-color="#4f4f4f" stop-opacity="0.9"/>
          <stop offset="1" stop-color="#5a5a5a" stop-opacity="0"/>
        </linearGradient>
      </defs>
      <path d="M0,168 C55,146 125,142 170,152 C185,200 195,260 200,299 L0,299 Z" fill="url(#panelFade)"/>
    </svg>

    <h1 class="headline">Do you handle snow and ice related slip and falls?</h1>
    <p class="intro">Darrel is one of the top snow industry experts in the country!</p>

    <div class="brand">The Frost<br>Counsel</div>

    <div class="credentials">
      <h2>DARREL'S CREDENTIALS:</h2>
      <ul>
        <li><svg width="8" height="8" viewBox="0 0 8 8"><circle cx="4" cy="4" r="4" fill="var(--tick)"/><path d="M2.2 4.1 L3.5 5.3 L5.9 2.8" stroke="#4a4a4a" stroke-width="1.1" fill="none"/></svg>Accredited Winter Practitioner (AWP)</li>
        <li><svg width="8" height="8" viewBox="0 0 8 8"><circle cx="4" cy="4" r="4" fill="var(--tick)"/><path d="M2.2 4.1 L3.5 5.3 L5.9 2.8" stroke="#4a4a4a" stroke-width="1.1" fill="none"/></svg>Past WRTA board member and chair</li>
        <li><svg width="8" height="8" viewBox="0 0 8 8"><circle cx="4" cy="4" r="4" fill="var(--tick)"/><path d="M2.2 4.1 L3.5 5.3 L5.9 2.8" stroke="#4a4a4a" stroke-width="1.1" fill="none"/></svg>Former ISO 9001 certified snow company owner</li>
        <li><svg width="8" height="8" viewBox="0 0 8 8"><circle cx="4" cy="4" r="4" fill="var(--tick)"/><path d="M2.2 4.1 L3.5 5.3 L5.9 2.8" stroke="#4a4a4a" stroke-width="1.1" fill="none"/></svg>32 years in the industry</li>
      </ul>
    </div>

    <footer class="contact-bar">
      <span class="contact-item"><strong>CALL US</strong>
        <svg width="10" height="10" viewBox="0 0 10 10" aria-hidden="true"><circle cx="5" cy="5" r="5" fill="#fff"/><path d="M3.2 2.5 L4.2 3.6 L3.7 4.3 C4.1 5.1 4.8 5.8 5.6 6.2 L6.3 5.7 L7.4 6.7 L6.8 7.5 C4.8 7.3 2.6 5.2 2.4 3.1 Z" fill="#000"/></svg>
        <span class="phone-number">(555) 284-3917</span></span>
      <span class="contact-item">
        <svg width="10" height="10" viewBox="0 0 10 10" aria-hidden="true"><circle cx="5" cy="5" r="5" fill="#fff"/><rect x="2.4" y="3.2" width="5.2" height="3.6" fill="none" stroke="#000" stroke-width="0.8"/><path d="M2.4 3.2 L5 5.2 L7.6 3.2" fill="none" stroke="#000" stroke-width="0.8"/></svg>
        darrel@thefrostcounsel.com</span>
      <span class="contact-item">
        <svg width="10" height="10" viewBox="0 0 10 10" aria-hidden="true"><circle cx="5" cy="5" r="4.4" fill="none" stroke="#fff" stroke-width="0.9"/><ellipse cx="5" cy="5" rx="1.9" ry="4.4" fill="none" stroke="#fff" stroke-width="0.8"/><path d="M0.8 5 H9.2" stroke="#fff" stroke-width="0.8"/></svg>
        www.thefrostcounsel.com</span>
    </footer>
  </section>

  <section class="postcard postcard--back">
    <div class="photo-area" role="img" aria-label="Blurred street photo of a man in jeans slipping on a wet icy pavement, his backpack falling to the ground"></div>

    <div class="brand">The Frost<br>Counsel</div>
    <p class="return-address">P.O. Box 418, Lakeview MI 48211 6</p>
    <div class="stamp-box" aria-label="Stamp area"></div>

    <footer class="contact-bar">
      <span class="contact-item"><strong>CALL US</strong>
        <svg width="10" height="10" viewBox="0 0 10 10" aria-hidden="true"><circle cx="5" cy="5" r="5" fill="#fff"/><path d="M3.2 2.5 L4.2 3.6 L3.7 4.3 C4.1 5.1 4.8 5.8 5.6 6.2 L6.3 5.7 L7.4 6.7 L6.8 7.5 C4.8 7.3 2.6 5.2 2.4 3.1 Z" fill="#000"/></svg>
        <span class="phone-number">(555) 284-3917</span></span>
      <span class="contact-item">
        <svg width="10" height="10" viewBox="0 0 10 10" aria-hidden="true"><circle cx="5" cy="5" r="5" fill="#fff"/><rect x="2.4" y="3.2" width="5.2" height="3.6" fill="none" stroke="#000" stroke-width="0.8"/><path d="M2.4 3.2 L5 5.2 L7.6 3.2" fill="none" stroke="#000" stroke-width="0.8"/></svg>
        darrel@thefrostcounsel.com</span>
      <span class="contact-item">
        <svg width="10" height="10" viewBox="0 0 10 10" aria-hidden="true"><circle cx="5" cy="5" r="4.4" fill="none" stroke="#fff" stroke-width="0.9"/><ellipse cx="5" cy="5" rx="1.9" ry="4.4" fill="none" stroke="#fff" stroke-width="0.8"/><path d="M0.8 5 H9.2" stroke="#fff" stroke-width="0.8"/></svg>
        www.thefrostcounsel.com</span>
    </footer>
  </section>

</body>
</html>
```